Info-graphic design

We need an info-graphic created showing how to easily paint new timber furniture from scratch. Our product is kit set furniture that can be decorated by the user - offering them some flexibility in how the final product can look.

The info-graphic needs to be easy to follow and have a fun/interesting look. I have attached a document showing the text that needs to appear on the info-graphic. On the document I have marked in red where graphic icons of different things are required.

Paint

```html
<!DOCTYPE html>
<html lang="en">
<head>
<meta charset="utf-8">
<title>Get Started – Painting</title>
<link rel="stylesheet" href="https://fonts.googleapis.com/css2?family=Luckiest+Guy&family=Open+Sans:wght@400;600;700&display=swap">
<style>
:root{
  --wood-light:#e9a25a;
  --wood-mid:#d98a45;
  --wood-dark:#c4743a;
  --plank-line:rgba(120,60,20,.28);
  --ink:#3b2211;
  --heading:#ffffff;
  --heading-edge:#7a3d14;
  --rule:rgba(255,255,255,.55);
  --panel:rgba(255,240,220,.18);
}
*{margin:0;padding:0;box-sizing:border-box}
html,body{width:849px;height:1200px;overflow:hidden}
body{
  position:relative;
  font-family:"Open Sans",Arial,sans-serif;
  color:var(--ink);
  background:
    repeating-linear-gradient(90deg,transparent 0 140px,var(--plank-line) 140px 142px),
    linear-gradient(180deg,var(--wood-light),var(--wood-mid) 50%,var(--wood-dark));
}
.title{
  position:absolute;top:16px;left:0;width:849px;text-align:center;
  font-family:"Luckiest Guy",cursive;font-size:52px;letter-spacing:2px;
  color:var(--heading);text-shadow:3px 3px 0 var(--heading-edge);
}
.heading{
  position:absolute;font-family:"Luckiest Guy",cursive;font-size:32px;
  color:var(--heading);letter-spacing:1px;
  text-shadow:2px 2px 0 var(--heading-edge),-1px -1px 0 var(--heading-edge);
}
.copy{position:absolute;font-size:11.5px;line-height:1.42}
.copy p+p{margin-top:7px}
.copy strong{font-weight:700}
.rule{position:absolute;left:24px;width:801px;border-top:2px dashed var(--rule)}
.required{position:absolute;left:30px;top:142px;font-weight:700;font-size:13px}
.kit{position:absolute;left:30px;top:166px;width:395px;display:grid;grid-template-columns:repeat(4,1fr);gap:10px 8px}
.kit-item{text-align:center;font-size:10px;font-weight:600}
.kit-swatch{height:62px;border-radius:6px;margin-bottom:4px;border:2px solid rgba(255,255,255,.6)}
.scene{position:absolute;border-radius:6px;border:2px solid rgba(255,255,255,.55)}
</style>
</head>
<body>

<h1 class="title">GET STARTED - PAINTING</h1>

<h2 class="heading" style="left:30px;top:100px">BEFORE YOU START</h2>
<div class="required">Required:</div>
<div class="kit">
  <div class="kit-item"><div class="kit-swatch" role="img" aria-label="Primer tin icon" style="background:linear-gradient(#9fb7c6,#5f7f94)"></div>Primer</div>
  <div class="kit-item"><div class="kit-swatch" role="img" aria-label="Topcoat tin icon" style="background:linear-gradient(#e7d3a8,#b9914e)"></div>Topcoat</div>
  <div class="kit-item"><div class="kit-swatch" role="img" aria-label="Sandpaper icon" style="background:linear-gradient(#d6b98a,#a07c4a)"></div>Sandpaper</div>
  <div class="kit-item"><div class="kit-swatch" role="img" aria-label="Paint tray and roller icon" style="background:linear-gradient(#c7d5dc,#6e8c9a)"></div>Paint Tray</div>
  <div class="kit-item"><div class="kit-swatch" role="img" aria-label="Clean rags icon" style="background:linear-gradient(#f1efe8,#bdb6a6)"></div>Clean Rags</div>
  <div class="kit-item"><div class="kit-swatch" role="img" aria-label="Protective clothing icon" style="background:linear-gradient(#a7c3d8,#4f7391)"></div>Protective Clothing</div>
  <div class="kit-item"><div class="kit-swatch" role="img" aria-label="Mask and goggles icon" style="background:linear-gradient(#e6e6e6,#8d8d8d)"></div>Mask/Goggles</div>
  <div class="kit-item"><div class="kit-swatch" role="img" aria-label="Ventilated area icon" style="background:linear-gradient(#cfe6f0,#7fb0c6)"></div>Ventilated Area</div>
</div>

<div class="copy" style="left:440px;top:104px;width:385px">
  <p><strong>MDF (Medium Density Fibreboard)</strong><br>MDF is absorbent and requires a primer or undercoat. This coat seals the MDF fibres and allows the topcoat to adhere to the board with good strength, resulting in a durable finish and a smooth, even look once the topcoat is applied over the surface.</p>
  <p><strong>Paints</strong><br>Primers and undercoats can be acrylic, latex or oil based. Acrylics are easier to work with and are ideal if you plan to use an acrylic based paint for the top coat. Acrylics can be thinned and cleaned up with water, which makes them less toxic, lower in odour, and better for the environment. Oil based primers give a more durable finish with better colour consistency, but require mineral turpentine or a similar solvent to clean up afterwards.</p>
</div>

<div class="rule" style="top:376px"></div>

<h2 class="heading" style="left:30px;top:390px">START</h2>
<div class="copy" style="left:30px;top:438px;width:215px">
  <p>Ensure you have a clean, tidy and safe working area. Put down drop sheets to protect floors. Your work area should be well ventilated, dry and free of dust before you begin.</p>
</div>
<div class="scene" role="img" aria-label="Illustration of a tidy, ventilated room with a window and drop sheet" style="left:255px;top:394px;width:170px;height:150px;background:linear-gradient(160deg,#f4e6cf,#c9b08a)"></div>

<h2 class="heading" style="left:440px;top:390px">PREPARE</h2>
<div class="copy" style="left:440px;top:436px;width:385px">
  <p>Remove all dust and debris from the MDF surface. Use a rough grit sandpaper such as 120 grit, then a fine grit sandpaper to achieve a finish that is really smooth. This will allow the undercoat to adhere. Pay special attention to the edges and ensure they are smooth so the primer will adhere.</p>
</div>
<div class="scene" role="img" aria-label="Illustration of a sanding block on a board" style="left:440px;top:545px;width:385px;height:66px;background:linear-gradient(90deg,#e8c99a,#b98a55)"></div>

<div class="rule" style="top:630px"></div>

<h2 class="heading" style="left:30px;top:645px">CLEAN</h2>
<div class="scene" role="img" aria-label="Illustration of a cloth wiping dust from a board" style="left:30px;top:690px;width:170px;height:190px;background:linear-gradient(180deg,#caa06a,#8e6236)"></div>
<div class="copy" style="left:215px;top:690px;width:210px">
  <p>Use a damp cloth to clean the MDF surfaces once sanded. This will ensure there are no loose particles on the surface and keep the undercoat adhesion. Remember MDF produces a fine dust when sanded, so take extra care to clean up all dust particles. It might be best to do this before the furniture is assembled. Allow the MDF to dry completely before beginning the next step.</p>
</div>

<h2 class="heading" style="left:440px;top:645px">SEAL</h2>
<div class="copy" style="left:440px;top:690px;width:385px">
  <p>Apply primer to all surfaces. When the surfaces have dried fully, sand with a fine sandpaper (120 grit). Apply a second coat of primer. Ensure the edges of the MDF are sealed well, as these are porous and most likely to absorb moisture.</p>
</div>
<div class="scene" role="img" aria-label="Illustration of a primer tin, brush and sandpaper" style="left:560px;top:790px;width:265px;height:95px;background:linear-gradient(90deg,#f0e7d8,#c7b597)"></div>

<div class="rule" style="top:910px"></div>

<h2 class="heading" style="left:30px;top:925px">TOPCOATS</h2>
<div class="copy" style="left:30px;top:970px;width:205px">
  <p>Once the primer has dried fully, topcoats can be applied. It is recommended that if you have used an acrylic primer, then use an acrylic topcoat. Likewise, if you used an oil based primer, use an oil based topcoat. Avoid overloading the brush or roller with paint. Apply a thin coat first, allow it to dry, then sand lightly. Apply a second coat for an even finish on all of the board.</p>
</div>
<div class="scene" role="img" aria-label="Illustration of a paint roller and tray applying topcoat to a board" style="left:250px;top:960px;width:175px;height:200px;background:linear-gradient(180deg,#e9e2d6,#9c8c74)"></div>

<h2 class="heading" style="left:440px;top:925px">FINISH</h2>
<div class="copy" style="left:440px;top:970px;width:170px">
  <p>Allow paint to fully dry (cure) as per the manufacturer's instructions for drying time. Dispose of any leftover paint responsibly.</p>
</div>
<div class="scene" role="img" aria-label="Illustration of finished painted furniture" style="left:625px;top:970px;width:200px;height:190px;background:linear-gradient(160deg,#c9dde6,#6b93a8)"></div>

</body>
</html>
```